Quirky Coffee Shop Loyalty Card

We need a new loyalty card in business card size format for our independent coffee shop. We are a quirky, ethically focussed, high quality coffee establishment with a focus on cutting edge products like siphon coffee and flamed latte brules. Projecting an image of high quality, innovation, ethical and eco-friendly with a quirky and unique feel. We would like a green background appearance, echoing or complementing the green in our logo (uploaded). Our coffee is organic and ethically sourced, we would like to communicate this - it doesn't need to be done in obvious way, open to creative suggestions. Earthy and straightforward in approach is important to us. We use cups made from 100% repurposed coffee husk, called Brindle (https://brindlecups.example/). One idea we had would be to have this cup image on the card with arrows pointing in from words like "Organic", "Made from coffee husks", "Ethical" etc... but in a less cliche'd way than this sounds!Please note that although this is a business card size, we need a loyalty card not a business card. On the back, we need to convey that the customer buys 8 coffees and gets the ninth free. We also need our social media links, email and address:
FB: @pebblekettlemossford
Insta: Pebblekettle
Email: mossford@pebblekettle.example
Address: No.4 Quill Row, ZX40 9KT
Phone: 01999 462057

Target Market(s)

All shop customers

Industry/Entity Type

Coffee Shop

Contact Information for Business Card

FB: @pebblekettlemossford
Insta: Pebblekettle
Phone: 01999 462057

Colors

Designer to choose colors to be used in the design.

Requirements
Must have
• Quirky, ethical, organic feel
Should not have
• Well-used or obvious coffee shop imagery

```html
<!DOCTYPE html>
<html lang="en">
<head>
<meta charset="utf-8">
<title>Pebblekettle Loyalty Card</title>
<link rel="stylesheet" href="https://fonts.googleapis.com/css2?family=Hind:wght@400;500&family=Kaushan+Script&display=swap">
<style>
  :root {
    --page: #3f3f3f;
    --earth: #8f4f0a;
    --olive: #7f8a1f;
    --leaf: #76b82a;
    --leaf-soft: #84a52a;
    --cream: #ffffff;
    --ink: #111111;
    --roast: #7a3f08;
  }
  html, body {
    margin: 0;
    width: 1200px;
    height: 1200px;
    overflow: hidden;
    background: var(--page);
  }
  .sheet {
    width: 1200px;
    height: 1200px;
    display: flex;
    flex-direction: column;
    align-items: center;
    justify-content: center;
    gap: 34px;
  }
  .card { width: 960px; height: 548px; display: block; }
  .contact-line {
    font-family: "Hind", sans-serif;
    font-size: 24px;
    font-weight: 400;
    fill: var(--ink);
  }
  .badge-name {
    font-family: "Hind", sans-serif;
    font-size: 19px;
    font-weight: 500;
    fill: var(--roast);
  }
  .ghost-name {
    font-family: "Hind", sans-serif;
    font-size: 78px;
    font-weight: 500;
    fill: var(--cream);
    opacity: 0.12;
  }
  .offer {
    font-family: "Kaushan Script", cursive;
    font-size: 46px;
    fill: var(--ink);
  }
</style>
</head>
<body>
<main class="sheet">

  <!-- Contact side -->
  <svg class="card card-contact" viewBox="0 0 730 417" xmlns="http://www.w3.org/2000/svg" aria-label="Loyalty card contact side">
    <defs><clipPath id="contact-clip"><rect width="730" height="417"/></clipPath></defs>
    <g clip-path="url(#contact-clip)">
      <rect width="730" height="417" fill="var(--earth)"/>
      <circle cx="700" cy="235" r="280" fill="var(--olive)"/>
      <circle cx="720" cy="235" r="215" fill="var(--leaf)"/>
      <circle cx="20" cy="20" r="60" fill="var(--leaf)"/>
      <circle cx="20" cy="20" r="90" fill="none" stroke="var(--leaf)" stroke-width="18" opacity="0.5"/>
      <path class="brush-band" d="M0 252 L520 262 L600 270 L420 296 L0 300 Z" fill="var(--leaf)" opacity="0.9"/>
      <circle cx="140" cy="170" r="330" fill="var(--cream)" opacity="0.2"/>
      <text class="ghost-name" x="20" y="205">Pebblekettle</text>

      <text class="contact-line" x="378" y="133" text-anchor="end">@pebblekettlemossford</text>
      <circle cx="404" cy="125" r="12" fill="var(--ink)"/>

      <text class="contact-line" x="378" y="176" text-anchor="end">Pebblekettle</text>
      <rect x="393" y="158" width="22" height="22" rx="5" fill="none" stroke="var(--ink)" stroke-width="2"/>

      <text class="contact-line" x="378" y="219" text-anchor="end">mossford@pebblekettle.example</text>
      <g fill="none" stroke="var(--ink)" stroke-width="1.6">
        <rect x="392" y="203" width="25" height="17"/>
        <path d="M392 203 L404.5 213 L417 203 M392 220 L401 211 M417 220 L408 211"/>
      </g>

      <text class="contact-line" x="378" y="262" text-anchor="end">No.4 Quill Row, ZX40 9KT</text>
      <path d="M404 267 C396 257 394 252 394 248 A10 10 0 0 1 414 248 C414 252 412 257 404 267 Z" fill="var(--ink)"/>
      <circle cx="404" cy="248" r="3.5" fill="var(--earth)"/>

      <text class="contact-line" x="378" y="304" text-anchor="end">01999 462057</text>
      <circle cx="404" cy="297" r="11" fill="none" stroke="var(--ink)" stroke-width="2"/>
      <path d="M399 292 L402 291 L404 295 L402 297 C403 299 404 300 406 301 L408 299 L412 301 L411 304 C405 304 399 298 399 292 Z" fill="var(--ink)"/>

      <circle cx="522" cy="215" r="70" fill="var(--cream)" stroke="var(--roast)" stroke-width="4"/>
      <text class="badge-name" x="522" y="222" text-anchor="middle">Pebblekettle</text>
    </g>
  </svg>

  <!-- Offer side -->
  <svg class="card card-offer" viewBox="0 0 730 417" xmlns="http://www.w3.org/2000/svg" aria-label="Loyalty card offer side">
    <defs><clipPath id="offer-clip"><rect width="730" height="417"/></clipPath></defs>
    <g clip-path="url(#offer-clip)">
      <rect width="730" height="417" fill="var(--earth)"/>
      <circle cx="370" cy="480" r="410" fill="var(--olive)"/>
      <circle cx="370" cy="480" r="345" fill="var(--leaf-soft)"/>
      <circle cx="380" cy="480" r="290" fill="var(--leaf)"/>
      <path class="brush-band" d="M0 38 C120 58 260 70 360 72 L730 44 L730 76 L420 104 C300 112 150 100 0 88 Z" fill="var(--leaf)"/>
      <path d="M0 96 L330 118 L0 112 Z" fill="var(--leaf)" opacity="0.35"/>

      <circle cx="366" cy="118" r="66" fill="var(--cream)" stroke="var(--roast)" stroke-width="4"/>
      <text class="badge-name" x="366" y="125" text-anchor="middle">Pebblekettle</text>

      <text class="offer" x="152" y="258">buy 8 coffees</text>
      <text class="offer" x="278" y="306">get 1 free coffee</text>
    </g>
  </svg>

</main>
</body>
</html>
```